Harbor Glow Living.com Landing Page

Create a well designed home/landing page using that communicates the feeling of Harbor Glow Living with this sections that scroll from top to bottom -
Top section - Displays "Harbor Glow Living" with space for embedded YouTube video.

The following sections follow the top section -
Assess your current Harbor Glow Living. Complete our free life balance assessment to identify key areas where you you will most benefit.
"Learn more" call to action button

Create a Harbor Glow Living Study Hub account. Get a 14 day free trial to a wealth of learning activities, motivational videos and professional presentations on our learning portal designed specifically to address the eight essential areas of Harbor Glow Living.
"Register now" call to action button

Get weekly reports on your progress and goal achievement. Celebrate your success each week as you review your progress on each life balance area.

Appropriate royalty free photos and graphics that fit the chosen theme you recommend.
Updates

I'm reviewing the designs. I realize that I need to clarify that Harbor Glow Living focuses on eight areas, not just physical fitness and meditation. Spirituality and Sense of Purpose; Fitness and Health; Relationships; Personal Finance; Recreation and Fun; Physical Environment; Personal Development and Learning; Work and Career

Number of Pages Required

1 page

Colors
33a6d7
00a990
9bcb3c
2f73b3

```html
<!DOCTYPE html>
<html lang="en">
<head>
<meta charset="utf-8">
<title>Harbor Glow Living</title>
<link href="https://fonts.googleapis.com/css2?family=Raleway:wght@400;500;600;700&display=swap" rel="stylesheet">
<style>
  :root {
    --green: #9bcb3c;
    --green-deep: #88b636;
    --green-light: #a9d152;
    --ink: #333333;
    --text: #3a3a3a;
    --border: #c9c9c9;
    --white: #ffffff;
    --tone-warm: #b08a70;
    --tone-warm-dark: #6e4e40;
    --tone-sand: #cbbba3;
    --tone-sand-dark: #8d7252;
    --tone-amber: #e7a95a;
    --tone-amber-dark: #c98560;
    --tone-slate: #9aa6b6;
    --tone-slate-dark: #6c7a90;
  }
  * { box-sizing: border-box; margin: 0; padding: 0; }
  html, body { width: 958px; height: 1200px; overflow: hidden; background: var(--white); }
  body { font-family: "Raleway", sans-serif; color: var(--text); position: relative; }

  .hero {
    position: absolute; left: 0; top: 0; width: 958px; height: 321px;
    background: linear-gradient(180deg, var(--green-light) 0%, #a3ce4c 50%, var(--green-deep) 100%);
    overflow: hidden;
  }
  .hero-backdrop { position: absolute; inset: 0; }
  .hero-title {
    position: absolute; left: 131px; top: 110px;
    font-size: 36px; line-height: 39px; font-weight: 600; color: var(--white);
    letter-spacing: 0.2px;
  }
  .video-frame {
    position: absolute; left: 509px; top: 64px; width: 317px; height: 195px;
    border: 2px solid var(--white);
    background: linear-gradient(180deg, var(--tone-warm) 0%, var(--tone-warm-dark) 100%);
  }
  .video-play { position: absolute; left: 138px; top: 76px; }

  .feature {
    position: absolute; left: 120px; width: 719px; height: 197px;
    border: 1px solid var(--border); border-radius: 2px; background: var(--white);
    overflow: hidden;
  }
  .feature-one { top: 385px; }
  .feature-two { top: 624px; }
  .feature-three { top: 863px; }
  .feature-photo { position: absolute; top: 0; width: 271px; height: 100%; }
  .feature-photo.left { left: 0; }
  .feature-photo.right { right: 0; }
  .photo-meadow { background: linear-gradient(180deg, var(--tone-sand) 0%, var(--tone-sand-dark) 100%); }
  .photo-sunset { background: linear-gradient(180deg, var(--tone-amber-dark) 0%, var(--tone-amber) 100%); }
  .photo-summit { background: linear-gradient(180deg, var(--tone-slate) 0%, var(--tone-slate-dark) 100%); }

  .feature-body { position: absolute; top: 0; height: 100%; padding-top: 33px; }
  .feature-one .feature-body, .feature-three .feature-body { left: 303px; width: 360px; }
  .feature-two .feature-body { left: 32px; width: 380px; }
  .feature-heading { font-size: 15px; line-height: 14.5px; font-weight: 500; color: var(--ink); margin-bottom: 15px; }
  .feature-text { font-size: 10.8px; line-height: 14.4px; font-weight: 500; color: var(--text); margin-bottom: 11px; }
  .button {
    display: inline-block; height: 26px; line-height: 26px; padding: 0 10px;
    border-radius: 13px; background: var(--green); color: var(--white);
    font-size: 9.6px; font-weight: 600; letter-spacing: 0.6px; text-decoration: none;
  }

  .footer {
    position: absolute; left: 0; top: 1103px; width: 958px; height: 97px;
    background: var(--green); color: var(--white);
  }
  .follow-label { position: absolute; left: 0; right: 0; top: 15px; text-align: center; font-size: 10.4px; font-weight: 600; letter-spacing: 0.3px; }
  .social { position: absolute; left: 407px; top: 34px; display: flex; gap: 11px; }
  .social a { display: block; width: 20px; height: 20px; border-radius: 50%; background: var(--white); }
  .footer-copy { position: absolute; left: 119px; top: 67px; font-size: 8.4px; }
  .footer-links { position: absolute; right: 120px; top: 67px; font-size: 8.4px; }
  .footer-links a { color: var(--white); text-decoration: none; }
</style>
</head>
<body>
  <header class="hero">
    <div class="hero-backdrop" role="img" aria-label="Group of friends jumping joyfully at the beach, tinted green"></div>
    <h1 class="hero-title">Harbor Glow<br>Living</h1>
    <div class="video-frame" role="img" aria-label="Embedded video: woman meditating on a deck at sunset">
      <svg class="video-play" width="40" height="40" viewBox="0 0 40 40" aria-hidden="true">
        <circle cx="20" cy="20" r="18.5" fill="none" stroke="#ffffff" stroke-width="2"/>
        <path d="M15 11 L29 20 L15 29 Z" fill="#ffffff"/>
      </svg>
    </div>
  </header>

  <section class="feature feature-one">
    <div class="feature-photo left photo-meadow" role="img" aria-label="Woman in a dress twirling in a meadow at golden hour"></div>
    <div class="feature-body">
      <h2 class="feature-heading">Assess your current Harbor Glow Living.</h2>
      <p class="feature-text">Complete our free life balance assessment to identify key areas where you you will most benefit.</p>
      <a class="button" href="#">Learn More</a>
    </div>
  </section>

  <section class="feature feature-two">
    <div class="feature-body">
      <h2 class="feature-heading">Create a Harbor Glow Living Study Hub account.</h2>
      <p class="feature-text">Get a 14 day free trial to a wealth of learning activities, motivational videos and professional presentations on our learning portal designed specifically to address the eight essential areas of Harbor Glow Living.</p>
      <a class="button" href="#">Register Now</a>
    </div>
    <div class="feature-photo right photo-sunset" role="img" aria-label="Silhouette of a woman with arms outstretched against a sunset over the sea"></div>
  </section>

  <section class="feature feature-three">
    <div class="feature-photo left photo-summit" role="img" aria-label="Man standing on a rocky summit with arms open under a cloudy sky"></div>
    <div class="feature-body">
      <h2 class="feature-heading">Get weekly reports on your progress and goal achievement.</h2>
      <p class="feature-text">Celebrate your success each week as you review your progress on each life balance area.</p>
      <a class="button" href="#">Learn More</a>
    </div>
  </section>

  <footer class="footer">
    <p class="follow-label">FOLLOW US</p>
    <nav class="social" aria-label="Social profiles">
      <a href="#" aria-label="Social profile one"></a>
      <a href="#" aria-label="Social profile two"></a>
      <a href="#" aria-label="Social profile three"></a>
      <a href="#" aria-label="Social profile four"></a>
      <a href="#" aria-label="Social profile five"></a>
    </nav>
    <p class="footer-copy">Harbor Glow Living.com © 2020. All Rights Reserved.</p>
    <p class="footer-links"><a href="#">Terms and Conditions</a> | <a href="#">Privacy Policy</a></p>
  </footer>
</body>
</html>
```